Briefpapier klangrabatt17
Die Zusammenarbeit war vorbildlich. Sehr schnelle Reaktion auf unsere Wünsche und eine sehr gute Umsetzung des Projektes. Danke, wir werden wieder auf Sie zurückkommen für unseren nächsten Flyer.
Zielgruppe
Wir verkaufen Musiknoten, Lehr-DVDs für Instrumente aus Klassik, Rock, Pop, Jazz etc.
Da wir in letzter Zeit mehr Musiknoten aus der Klassik haben, wäre es sinnvoll, den Briefbogen seriös zu gestalten.
Aufgabenstellung
Wir bitten um Gestaltung eines Briefbogens mit den folgenden Informationen:
Anschrift: klangrabatt17
www.klangrabatt17.example
Wir haben folgende Homepage:
http://laden.tonfinder.example/38527/Home.html
Der Zusatz lyra digital sollte allerdings nicht im Brieflogo erscheinen.
Also Logo nur mit "klangrabatt17" und dem Zusatz: Ihr Spezialist für Musiknoten und Lehr-DVD's
Bitte die in der angefügten Datei verwandten Farben verwenden (gelb und rot)

```html
<!DOCTYPE html>
<html lang="de">
<head>
<meta charset="utf-8">
<title>Briefpapier klangrabatt17</title>
<link rel="stylesheet" href="https://fonts.googleapis.com/css2?family=Source+Sans+3:wght@400;700&display=swap">
<style>
  :root {
    --bg: #f7f7f7;
    --paper: #ffffff;
    --olive: #c9c11e;
    --olive-cap: #d3c924;
    --cream: #e6e5c3;
    --red: #c8242e;
    --grey-text: #9a9a8a;
    --dark-text: #333333;
    --rule: #8a8a8a;
  }
  html, body { margin: 0; padding: 0; }
  body {
    width: 1200px; height: 1000px; overflow: hidden;
    background: var(--bg);
    font-family: "Source Sans 3", sans-serif;
    position: relative;
  }
  .letterhead {
    position: absolute; left: 29px; top: 111px;
    width: 533px; height: 753px;
    background: var(--paper);
    box-shadow: 3px 3px 6px rgba(0,0,0,.35);
    overflow: hidden;
  }
  .side-band {
    position: absolute; left: 520px; top: 28px;
    width: 13px; height: 260px; background: var(--cream);
  }
  .brand-name {
    position: absolute; margin: 0;
    font-weight: 700; color: var(--olive);
    letter-spacing: -0.5px; line-height: 1;
    white-space: nowrap;
  }
  .letterhead .brand-name { left: 284px; top: 35px; font-size: 31px; }
  .contact { position: absolute; left: 403px; font-size: 7.5px; line-height: 10px; color: var(--grey-text); white-space: nowrap; }
  .contact-address { top: 84px; }
  .contact-lines { top: 123px; }
  .contact-row { display: flex; align-items: flex-start; gap: 4px; height: 13px; }
  .contact-row svg { flex: none; }
  .contact .person { color: var(--red); }
  .return-line {
    position: absolute; left: 121px; top: 147px; margin: 0;
    font-size: 7.5px; color: var(--dark-text);
  }
  .return-line .dot { display: inline-block; width: 4px; height: 4px; border-radius: 50%; background: var(--red); margin: 0 2px 1px; }
  .fold-mark { position: absolute; left: 0; width: 21px; height: 0; border-top: 1px solid var(--rule); }
  .fold-mark.upper { top: 263px; }
  .fold-mark.lower { top: 501px; }
  .footer-note {
    position: absolute; top: 703px; margin: 0; font-size: 7px; line-height: 8.5px;
    color: var(--grey-text);
  }
  .footer-note.bank { left: 15px; }
  .footer-note.legal { right: 25px; top: 711px; text-align: right; }
  .footer-band { position: absolute; left: 0; top: 728px; }
  .footer-url {
    position: absolute; left: 182px; top: 737px; width: 167px; margin: 0;
    text-align: center; font-size: 10px; line-height: 12px; color: #ffffff; white-space: nowrap;
  }
  .envelope { position: absolute; }
  .envelope.front { left: 599px; top: 133px; width: 562px; height: 386px; }
  .envelope.back { left: 599px; top: 538px; width: 563px; height: 293px; }
  .envelope svg.shape { position: absolute; left: 0; top: 0; }
  .envelope .sender { position: absolute; left: 44px; top: 136px; font-size: 8px; line-height: 10px; color: var(--grey-text); }
  .envelope .sender .person { color: var(--red); }
  .envelope .pin { position: absolute; left: 29px; top: 139px; }
  .envelope .brand-name { left: 311px; top: 300px; font-size: 36px; }
</style>
</head>
<body>

<section class="letterhead" aria-label="Briefbogen">
  <div class="side-band"></div>
  <h1 class="brand-name">klangrabatt17</h1>

  <div class="contact contact-address">
    <div class="contact-row">
      <svg width="13" height="13" viewBox="0 0 13 13"><rect x=".5" y=".5" width="12" height="12" rx="2" fill="none" stroke="var(--red)" stroke-width=".8"/><path d="M6.5 2.5a2.6 2.6 0 0 1 2.6 2.6c0 2-2.6 5-2.6 5s-2.6-3-2.6-5a2.6 2.6 0 0 1 2.6-2.6z" fill="var(--grey-text)"/><circle cx="6.5" cy="5.1" r="1" fill="#fff"/></svg>
      <div><span class="person">Matthias Kerner</span><br>Ahornweg 8<br>85099 Talbach</div>
    </div>
  </div>

  <div class="contact contact-lines">
    <div class="contact-row">
      <svg width="13" height="12" viewBox="0 0 13 12"><rect x=".5" y=".5" width="12" height="11" rx="2" fill="none" stroke="var(--red)" stroke-width=".8"/><path d="M3 4.5c0-1 7-1 7 0v1H8.5V4.8h-4v.7H3z M4 6h5l1 3H3z" fill="var(--grey-text)"/></svg>
      <span>08451-2846</span>
    </div>
    <div class="contact-row">
      <svg width="13" height="12" viewBox="0 0 13 12"><rect x=".5" y=".5" width="12" height="11" rx="2" fill="none" stroke="var(--red)" stroke-width=".8"/><rect x="3.5" y="3" width="6" height="6.5" fill="none" stroke="var(--grey-text)" stroke-width=".8"/><path d="M5 5h3M5 6.5h3M5 8h3" stroke="var(--grey-text)" stroke-width=".6"/></svg>
      <span>08451-61730</span>
    </div>
    <div class="contact-row">
      <svg width="13" height="12" viewBox="0 0 13 12"><rect x=".5" y=".5" width="12" height="11" rx="2" fill="none" stroke="var(--red)" stroke-width=".8"/><text x="6.5" y="8.8" font-size="8" text-anchor="middle" fill="var(--grey-text)" font-family="Source Sans 3, sans-serif">@</text></svg>
      <span>info@klangrabatt17.example</span>
    </div>
    <div class="contact-row">
      <svg width="13" height="12" viewBox="0 0 13 12"><rect x=".5" y=".5" width="12" height="11" rx="2" fill="none" stroke="var(--red)" stroke-width=".8"/><circle cx="6.5" cy="6" r="3" fill="none" stroke="var(--grey-text)" stroke-width=".8"/><path d="M3.5 6h6M6.5 3c-1.5 1.5-1.5 4.5 0 6M6.5 3c1.5 1.5 1.5 4.5 0 6" fill="none" stroke="var(--grey-text)" stroke-width=".5"/></svg>
      <span>www.klangrabatt17.example</span>
    </div>
  </div>

  <p class="return-line">Ahornweg 8<span class="dot"></span>85099 Talbach</p>

  <div class="fold-mark upper"></div>
  <div class="fold-mark lower"></div>

  <p class="footer-note bank">Bankverbindung:<br>Matthias Kerner Sparkasse Talbach<br>BIC:&nbsp;&nbsp;&nbsp;TLBADEM1XXX<br>IBAN: DE00 1234 5678 0000 4321 00</p>
  <p class="footer-note legal">Geschäftsführer: Matthias Kerner<br>Steuernummer: 123-456-78901<br>UST-ID-Nr. DE 000123456</p>

  <svg class="footer-band" width="533" height="25" viewBox="0 0 533 25">
    <rect x="0" y="14" width="533" height="11" fill="var(--cream)"/>
    <path d="M174 14 L360 14 L368 25 L166 25 Z" fill="var(--paper)"/>
    <path d="M182 25 C190 10 210 4 240 4 L292 4 C322 4 342 10 349 25 Z" fill="var(--olive-cap)"/>
  </svg>
  <p class="footer-url">www.klangrabatt17.example</p>
</section>

<section class="envelope front" aria-label="Briefumschlag Vorderseite">
  <svg class="shape" width="562" height="386" viewBox="0 0 562 386">
    <path d="M0 98 L0 70 C0 55 15 48 32 45 L262 1 C272 -1 290 -1 300 1 L530 48 C548 52 561 62 561 75 L561 98 Z" fill="var(--cream)"/>
    <rect x="1" y="98" width="560" height="286" fill="var(--paper)" style="filter:drop-shadow(1px 1px 1px rgba(0,0,0,.35))"/>
    <line x1="0" y1="98" x2="561" y2="98" stroke="var(--rule)" stroke-width="1.2"/>
    <rect x="40" y="253" width="223" height="88" rx="10" fill="var(--paper)" stroke="#bdbdbd" stroke-width="1"/>
  </svg>
  <svg class="pin" width="12" height="17" viewBox="0 0 12 17"><path d="M6 0a6 6 0 0 1 6 6c0 4-6 11-6 11S0 10 0 6a6 6 0 0 1 6-6z" fill="var(--olive)"/><circle cx="6" cy="6" r="2.2" fill="#fff"/></svg>
  <div class="sender"><span class="person">Matthias Kerner</span><br>Ahornweg 8<br>85099 Talbach</div>
  <p class="brand-name">klangrabatt17</p>
</section>

<section class="envelope back" aria-label="Briefumschlag Rückseite">
  <svg class="shape" width="563" height="293" viewBox="0 0 563 293">
    <rect x="1" y="0" width="561" height="290" fill="var(--paper)" style="filter:drop-shadow(1px 1px 1px rgba(0,0,0,.35))"/>
    <path d="M0 0 L562 0 L562 20 C562 35 548 48 530 51 L300 97 C290 99 272 99 262 97 L32 52 C15 48 0 38 0 22 Z" fill="var(--cream)"/>
  </svg>
</section>

</body>
</html>
```